Business Cards used to invite people to our church

We are a church and have need of a business card sized advertisement that allows our members to hand them out in order to invite people to the church. I need the front of the card to say "You're Invited" or "Come Check us out". with the service times on the back of the card later.
I have attached one of the OLD cards we have used in the past, but we want a complete makeover, into a more modern style that does not require the image.
I am also replacing the old logo with a newer "flat" logo which is attached.
Please use marketing colors. (blue or red or something that catches attention)
Create a card that DOES NOT have the picture of the two people on the front
The information on the sample card back is correct to go onto new card
Target Market(s)
anyone
Industry/Entity Type
Business
Contact Information for Business Card
sertice times and address information which you can get from the sample card I uploaded. It should have "You're Invited" or "Come Check us out" on the front of the card with out logo.

```html
<!DOCTYPE html>
<html lang="en">
<head>
<meta charset="utf-8">
<title>Grace Harbor Ministries – Invitation Card</title>
<link rel="stylesheet" href="https://fonts.googleapis.com/css2?family=Arimo:wght@400;700&family=Great+Vibes&display=swap">
<style>
  :root {
    --sky: #00aeef;
    --signal-red: #ed1c24;
    --deep-red: #9e1b1e;
    --white: #ffffff;
    --ink: #000000;
  }
  html, body {
    margin: 0;
    padding: 0;
    overflow: hidden;
    background: var(--white);
  }
  .card-sheet {
    position: relative;
    width: 1029px;
    height: 1200px;
    overflow: hidden;
    font-family: "Arimo", Arial, sans-serif;
    color: var(--white);
    background: var(--sky);
  }

  /* ---------- Front ---------- */
  .card-front {
    position: absolute;
    left: 0; top: 0;
    width: 1029px;
    height: 600px;
    background: var(--sky);
  }
  .front-waves {
    position: absolute;
    inset: 0;
    width: 1029px;
    height: 600px;
  }
  .corner-name {
    position: absolute;
    left: 57px;
    top: 56px;
    margin: 0;
    font-weight: 700;
    font-size: 40px;
    line-height: 1;
    color: var(--white);
    white-space: nowrap;
  }
  .brand-name {
    position: absolute;
    left: 46px;
    top: 334px;
    margin: 0;
    display: flex;
    align-items: center;
    gap: 10px;
    font-weight: 700;
    font-size: 33px;
    line-height: 1;
    color: var(--deep-red);
    white-space: nowrap;
  }
  .brand-name .brand-dot {
    width: 15px;
    height: 15px;
    border-radius: 50%;
    background: var(--deep-red);
  }
  .invite-line {
    position: absolute;
    left: 664px;
    top: 170px;
    width: 330px;
    margin: 0;
    font-family: "Great Vibes", cursive;
    font-weight: 400;
    font-size: 72px;
    line-height: 56px;
    color: var(--white);
  }
  .invite-line span { display: block; }
  .invite-line .second { padding-left: 92px; }
  .pastors {
    position: absolute;
    right: 25px;
    top: 545px;
    margin: 0;
    font-weight: 700;
    font-size: 25px;
    line-height: 1.1;
    color: var(--white);
    white-space: nowrap;
  }
  .card-divider {
    position: absolute;
    left: 0; top: 600px;
    width: 1029px;
    height: 7px;
    background: var(--ink);
  }

  /* ---------- Back ---------- */
  .card-back {
    position: absolute;
    left: 0; top: 607px;
    width: 1029px;
    height: 593px;
    background: var(--sky);
  }
  .edge-stripes {
    position: absolute;
    left: 33px;
    top: 0;
    width: 40px;
    height: 593px;
    background: linear-gradient(to right,
      var(--signal-red) 0 11px,
      var(--white) 11px 14px,
      var(--signal-red) 14px 20px,
      var(--white) 20px 23px,
      var(--signal-red) 23px 30px,
      var(--white) 30px 33px,
      var(--signal-red) 33px 40px);
  }
  .contact-block {
    position: absolute;
    left: 0;
    top: 62px;
    width: 1029px;
    padding-left: 80px;
    box-sizing: border-box;
    text-align: center;
    font-size: 41px;
    line-height: 50px;
    text-transform: uppercase;
    white-space: nowrap;
  }
  .contact-block p { margin: 0; }
  .service-times {
    position: absolute;
    left: 181px;
    top: 408px;
    width: 740px;
    margin: 0;
    padding: 0;
    list-style: none;
    font-size: 38px;
    line-height: 48px;
    text-transform: uppercase;
  }
  .service-times li {
    display: flex;
    align-items: baseline;
    white-space: nowrap;
  }
  .service-times .leader {
    flex: 1;
    overflow: hidden;
    margin: 0 6px 0 2px;
  }
  .service-times .leader::before {
    content: "....................................................................";
    letter-spacing: 1px;
  }
</style>
</head>
<body>
<main class="card-sheet">

  <section class="card-front">
    <svg class="front-waves" viewBox="0 0 1029 600" aria-hidden="true">
      <path d="M0 0 H1029 V8 C820 40 600 90 400 130 C250 160 110 155 0 140 Z" fill="var(--signal-red)"/>
      <path d="M0 150 C120 168 260 172 410 142 C610 100 820 50 1029 20" fill="none" stroke="var(--white)" stroke-width="8"/>
      <path d="M0 164 C130 182 270 184 420 154 C620 112 830 62 1029 34" fill="none" stroke="var(--signal-red)" stroke-width="5"/>
      <path d="M0 178 C140 194 280 196 430 166 C630 124 840 76 1029 48" fill="none" stroke="var(--white)" stroke-width="5"/>
      <path d="M0 585 C180 590 330 540 520 490 C700 445 860 425 1029 430 V600 H0 Z" fill="var(--white)"/>
      <path d="M0 592 C190 596 340 548 530 500 C710 456 870 438 1029 442 V600 H0 Z" fill="var(--signal-red)"/>
      <path d="M0 575 C170 578 320 530 510 480 C690 434 850 412 1029 416" fill="none" stroke="var(--signal-red)" stroke-width="5"/>
      <path d="M0 566 C160 568 310 520 500 470 C680 422 840 400 1029 402" fill="none" stroke="var(--white)" stroke-width="5"/>
    </svg>

    <p class="corner-name">GRACE HARBOR</p>

    <p class="invite-line"><span>You're</span><span class="second">Invited!</span></p>

    <p class="brand-name"><span class="brand-dot"></span>GRACE HARBOR MINISTRIES</p>

    <p class="pastors">PASTOR DANIEL &amp; RENEE WHITFIELD</p>
  </section>

  <div class="card-divider"></div>

  <section class="card-back">
    <div class="edge-stripes" aria-hidden="true"></div>

    <div class="contact-block">
      <p>graceharbor.org</p>
      <p>2480 W. Cedar Lane - Riverton, TX 75390</p>
    </div>

    <ul class="service-times">
      <li><span>Sunday</span><span class="leader"></span><span>09:00 AM</span></li>
      <li><span>Sunday</span><span class="leader"></span><span>11:00 AM</span></li>
      <li><span>Web. Bible Class</span><span class="leader"></span><span>07:00 PM</span></li>
    </ul>
  </section>

</main>
</body>
</html>
```